Conceptual Model Diagram for Replacing Medication with Behavior to Support Weight Loss Maintenance

Design a figure of a conceptual model that needs to be inserted into a word document for a QDV grant. This conceptual model illustrates how behavioral strategies can replace the regulatory functions lost after AOM discontinuation. The intervention targets three core vulnerabilities—appetite resurgence, metabolic inflexibility, and suboptimal mindstate—through the domains of Food, Physical Activity, and Mind. Sustained weight loss maintenance occurs at the intersection of these domains. The intervention is delivered within a design framework that makes behaviors easier to perform, aligns them with identity, and reinforces them through virtual support and community, ensuring real-world feasibility and long-term adherence.
Target Market(s)
QDV reviewers
Industry/Entity Type
academic
Font styles to use
Other font styles liked:
- arial
Requirements
Must have
- see my attached description

```html
<!DOCTYPE html>
<html lang="en">
<head>
<meta charset="utf-8">
<title>Conceptual Model for Replacing Medication with Behavior to Support Weight Loss Maintenance</title>
<link rel="stylesheet" href="https://fonts.googleapis.com/css2?family=Archivo+Black&family=Arimo:wght@400;700&display=swap">
<style>
  :root {
    --bg: #f1f5f6;
    --ink: #22574a;
    --muted: #7f8c8a;
    --label: #111111;
    --purple: #c77dff;
    --purple-text: #c05ef0;
    --purple-fill: #e9dff5;
    --purple-deep: #e2cdf8;
    --pink: #e88a96;
    --pink-text: #d45b6c;
    --pink-fill: #f1e1e3;
    --pink-deep: #efcfd6;
    --green: #66f2b8;
    --green-text: #5de8b4;
    --green-fill: #d6f5e9;
    --green-deep: #c0f3de;
    --core-fill: #dce4e3;
    --core-line: #8a9d99;
  }
  html, body {
    margin: 0;
    width: 1200px;
    height: 1200px;
    overflow: hidden;
    background: var(--bg);
  }
  .canvas { display: block; width: 1200px; height: 1200px; }
  .title { font-family: "Archivo Black", "Arial Black", sans-serif; font-size: 34px; fill: var(--ink); letter-spacing: 1.2px; }
  .domain { font-family: "Arimo", Arial, sans-serif; font-weight: 700; font-size: 30px; fill: var(--ink); }
  .core-text { font-family: "Arimo", Arial, sans-serif; font-weight: 700; font-size: 30px; fill: var(--ink); }
  .vuln { font-family: "Arimo", Arial, sans-serif; font-weight: 700; font-size: 34px; }
  .vuln-appetite { fill: var(--purple-text); }
  .vuln-mind { fill: var(--pink-text); }
  .vuln-metabolic { fill: var(--green-text); }
  .arc-label { font-family: "Arimo", Arial, sans-serif; font-weight: 700; font-size: 25px; fill: var(--label); }
  .legend-head { font-family: "Arimo", Arial, sans-serif; font-weight: 700; font-size: 29px; fill: var(--ink); }
  .legend-sub { font-family: "Arimo", Arial, sans-serif; font-weight: 700; font-size: 24px; fill: var(--muted); }
  .gap { fill: none; stroke: var(--bg); stroke-width: 18; }
</style>
</head>
<body>
<svg class="canvas" viewBox="0 0 1932 1932" xmlns="http://www.w3.org/2000/svg">
  <defs>
    <clipPath id="clip-top"><circle cx="970" cy="720" r="275"/></clipPath>
    <clipPath id="clip-left"><circle cx="808" cy="945" r="275"/></clipPath>
    <path id="arc-easy" d="M728,551 A295,295 0 0,1 894,435"/>
    <path id="arc-virtual" d="M518,1080 A320,320 0 0,0 968,1222"/>
    <path id="arc-identity" d="M1122,1263 A318,318 0 0,0 1358,1170"/>
  </defs>

  <text class="title" x="966" y="158" text-anchor="middle">Conceptual Model for Replacing Medication with Behavior to Support Weight Loss Maintenance</text>

  <g class="venn">
    <!-- region fills -->
    <circle cx="1133" cy="945" r="275" fill="var(--green-fill)"/>
    <circle cx="808" cy="945" r="275" fill="var(--pink-fill)"/>
    <circle cx="970" cy="720" r="275" fill="var(--purple-fill)"/>
    <circle cx="808" cy="945" r="275" fill="var(--pink-fill)" clip-path="url(#clip-top)"/>
    <circle cx="1133" cy="945" r="275" fill="var(--green-fill)" clip-path="url(#clip-left)"/>

    <!-- domain bands -->
    <path class="band-food" fill="var(--purple-deep)" d="M775,610 A228,228 0 0,1 1165,610 Q1050,600 970,650 Q890,600 775,610 Z"/>
    <path class="band-mind" fill="var(--pink-deep)" d="M640,795 A225,225 0 0,0 872,1160 Q800,1060 803,1010 Q680,930 640,795 Z"/>
    <path class="band-activity" fill="var(--green-deep)" d="M1298,795 A225,225 0 0,1 1068,1160 Q1135,1060 1138,1010 Q1260,930 1298,795 Z"/>

    <!-- outlines -->
    <circle class="gap" cx="1133" cy="945" r="275"/>
    <circle class="gap" cx="808" cy="945" r="275"/>
    <circle class="gap" cx="970" cy="720" r="275"/>
    <circle cx="1133" cy="945" r="275" fill="none" stroke="var(--green)" stroke-width="6"/>
    <circle cx="808" cy="945" r="275" fill="none" stroke="var(--pink)" stroke-width="6"/>
    <circle cx="970" cy="720" r="275" fill="none" stroke="var(--purple)" stroke-width="6"/>

    <!-- core -->
    <path d="M970,725 A275,275 0 0,1 1082,970 A275,275 0 0,1 858,970 A275,275 0 0,1 970,725 Z" fill="none" stroke="var(--bg)" stroke-width="20"/>
    <path d="M970,725 A275,275 0 0,1 1082,970 A275,275 0 0,1 858,970 A275,275 0 0,1 970,725 Z" fill="var(--core-fill)" stroke="var(--core-line)" stroke-width="6"/>
    <text class="core-text" text-anchor="middle">
      <tspan x="970" y="840">Sustained</tspan>
      <tspan x="970" y="873">Weight</tspan>
      <tspan x="970" y="906">Loss</tspan>
      <tspan x="970" y="940">Maintenance</tspan>
    </text>

    <text class="domain" x="970" y="579" text-anchor="middle">Food</text>
    <text class="domain" x="700" y="1035" text-anchor="middle">Mind</text>
    <text class="domain" text-anchor="middle"><tspan x="1250" y="1018">Physical</tspan><tspan x="1256" y="1052">Activity</tspan></text>

    <!-- icons -->
    <g class="icon-mind">
      <circle cx="798" cy="785" r="38" fill="none" stroke="var(--pink)" stroke-width="3"/>
      <circle cx="798" cy="785" r="22" fill="var(--pink-text)" role="img" aria-label="Brain icon"/>
    </g>
    <g class="icon-food" fill="var(--purple-text)">
      <circle cx="1143" cy="785" r="38" fill="none" stroke="var(--purple)" stroke-width="3"/>
      <rect x="1128" y="763" width="3" height="18"/>
      <rect x="1133" y="763" width="3" height="18"/>
      <rect x="1138" y="763" width="3" height="18"/>
      <rect x="1127" y="778" width="15" height="6" rx="3"/>
      <rect x="1131.5" y="782" width="6" height="26" rx="3"/>
      <ellipse cx="1153" cy="772" rx="7" ry="10"/>
      <rect x="1150" y="778" width="6" height="30" rx="3"/>
    </g>
    <g class="icon-activity">
      <circle cx="970" cy="1075" r="38" fill="none" stroke="var(--green)" stroke-width="3"/>
      <circle cx="970" cy="1075" r="22" fill="var(--green-text)" role="img" aria-label="Runner icon"/>
    </g>

    <!-- vulnerabilities -->
    <text class="vuln vuln-appetite" text-anchor="middle"><tspan x="970" y="312">Appetite</tspan><tspan x="970" y="351">Resurgence</tspan></text>
    <line x1="970" y1="375" x2="970" y2="434" stroke="var(--purple)" stroke-width="3"/>
    <circle cx="970" cy="445" r="11" fill="var(--bg)" stroke="var(--purple)" stroke-width="3"/>

    <text class="vuln vuln-mind" text-anchor="end"><tspan x="458" y="1015">Suboptimal</tspan><tspan x="458" y="1054">Mindstate</tspan></text>
    <line x1="474" y1="1025" x2="534" y2="1025" stroke="var(--pink)" stroke-width="3"/>
    <circle cx="545" cy="1025" r="11" fill="var(--bg)" stroke="var(--pink)" stroke-width="3"/>

    <text class="vuln vuln-metabolic" text-anchor="start"><tspan x="1480" y="1015">Metabolic</tspan><tspan x="1480" y="1054">Inflexibility</tspan></text>
    <line x1="1406" y1="1025" x2="1467" y2="1025" stroke="var(--green)" stroke-width="3"/>
    <circle cx="1395" cy="1025" r="11" fill="var(--bg)" stroke="var(--green)" stroke-width="3"/>

    <!-- framework labels -->
    <text class="arc-label"><textPath href="#arc-easy">Make it Easy</textPath></text>
    <text class="arc-label"><textPath href="#arc-virtual">Virtual Support and Social Connection</textPath></text>
    <text class="arc-label"><textPath href="#arc-identity">Align with identity</textPath></text>
  </g>

  <g class="legend">
    <rect x="666" y="1390" width="600" height="336" rx="22" fill="var(--core-fill)" stroke="var(--core-line)" stroke-width="5"/>
    <text class="legend-head" x="690" y="1436">Make it Easy</text>
    <text class="legend-sub" x="690" y="1475">Habits, routines, environment, low friction</text>
    <text class="legend-head" x="690" y="1547">Align with identity</text>
    <text class="legend-sub" x="690" y="1586">Self concept, maintain IT model, internalization</text>
    <text class="legend-head" x="690" y="1658">Virtual Support and Social Connection</text>
    <text class="legend-sub" x="690" y="1697">Accessibility, community, shared accountability</text>
  </g>
</svg>
</body>
</html>
```